IT CEO and Real Estate Investor

It should include two roles and be a two sided card (both roles can be one a single side with a creative view or on different sides).
Card must be creative and interesting, but still professional.
Phone countries(USA/Russia) might be as flags or words, whatever works better.
Boris Melnovetz
plain circle icon: boris_m
E-mail: melnovetz@quorbamail.com
plain square icon: plavbook.example/melnovetz
plain square icon: trelnet.example/in/melnovetz
Phone (US): 1(555)316-2947
Phone (RUS): 7(955)482-3170
First role:
Pex Lattor (pexlattor.example) - include logo or part of logo (the $)
E-Commerce Automation Solutions
Founder/CEO/CTO
Second role:
Real Estate Investor
Marrowfield, QT
UPDATE:
Let's do one side as logo only and all information on the other side - I don't like designs with information on both sides.
I also really liked designs on black (or other dark) background

```html
<!DOCTYPE html>
<html lang="en">
<head>
<meta charset="utf-8">
<title>Pex Lattor – Business Card</title>
<link href="https://fonts.googleapis.com/css2?family=Source+Sans+3:wght@400;600&display=swap" rel="stylesheet">
<style>
  :root {
    --backdrop: #4a3638;
    --card-dark: #231f20;
    --card-light: #ffffff;
    --brand-blue: #27aae1;
    --ink: #3b3b3b;
  }
  * { margin: 0; padding: 0; box-sizing: border-box; }
  html, body { width: 1200px; height: 1200px; overflow: hidden; }
  body {
    background: var(--backdrop);
    font-family: "Source Sans 3", "Myriad Pro", sans-serif;
    position: relative;
  }
  .card {
    position: absolute;
    left: 254px;
    width: 693px;
    height: 394px;
    border-radius: 20px;
    box-shadow: 0 6px 14px rgba(0,0,0,0.35);
  }
  .card--front { top: 174px; background: var(--card-dark); }
  .card--back { top: 634px; height: 393px; background: var(--card-light); }

  .brand {
    position: absolute;
    display: flex;
    align-items: center;
    color: var(--brand-blue);
    font-weight: 600;
    text-transform: uppercase;
    white-space: nowrap;
  }
  .brand__mark { background: var(--brand-blue); border-radius: 8px; flex: none; }
  .card--front .brand {
    left: 50%; top: 50%;
    transform: translate(-50%, -50%);
    font-size: 50px; letter-spacing: 6px; gap: 26px;
  }
  .card--front .brand__mark { width: 88px; height: 88px; border-radius: 12px; }
  .card--back .brand {
    left: 56px; top: 200px;
    transform: translateY(-50%);
    font-size: 25px; letter-spacing: 2px; gap: 12px;
  }
  .card--back .brand__mark { width: 48px; height: 48px; border-radius: 7px; }

  .divider {
    position: absolute;
    left: 311px; top: 34px;
    width: 2px; height: 318px;
    background: var(--brand-blue);
  }
  .divider__accent {
    position: absolute;
    left: 311px; top: 50px;
    width: 9px; height: 27px;
    background: var(--brand-blue);
  }
  .details {
    position: absolute;
    left: 338px; top: 46px;
    color: var(--ink);
    font-size: 18px;
    line-height: 23.2px;
  }
  .details__name {
    color: var(--brand-blue);
    font-size: 27px;
    font-weight: 400;
    line-height: 32px;
  }
  .details__role { margin-bottom: 17px; }
  .contacts { list-style: none; margin-bottom: 19px; }
  .contacts li { display: flex; align-items: center; gap: 8px; }
  .contacts svg { width: 17px; height: 17px; flex: none; }
</style>
</head>
<body>
  <section class="card card--front">
    <div class="brand"><span class="brand__mark"></span>Pex Lattor</div>
  </section>

  <section class="card card--back">
    <div class="brand"><span class="brand__mark"></span>Pex Lattor</div>
    <div class="divider"></div>
    <div class="divider__accent"></div>

    <div class="details">
      <h1 class="details__name">Boris Melnovetz</h1>
      <p class="details__role">E-Commerce Automation Solutions<br>Founder/CEO/CTO</p>

      <ul class="contacts">
        <li><svg viewBox="0 0 16 16"><circle cx="8" cy="8" r="7" fill="#27aae1"/></svg>boris_m</li>
        <li><svg viewBox="0 0 16 16"><rect x="1" y="3.5" width="14" height="9" fill="#27aae1"/><path d="M1.5 4 L8 9 L14.5 4 M1.5 12 L6 8 M14.5 12 L10 8" stroke="#fff" stroke-width="1.2" fill="none"/></svg>melnovetz@quorbamail.com</li>
        <li><svg viewBox="0 0 16 16"><rect x="1.5" y="1.5" width="13" height="13" fill="#27aae1"/></svg>plavbook.example/melnovetz</li>
        <li><svg viewBox="0 0 16 16"><rect x="1.5" y="1.5" width="13" height="13" fill="#27aae1"/></svg>trelnet.example/in/melnovetz</li>
        <li><svg viewBox="0 0 16 16"><path d="M1 7 Q8 1 15 7 L13 9 L11 7.5 L11 6 Q8 5 5 6 L5 7.5 L3 9 Z" fill="#27aae1"/><rect x="3.5" y="9.5" width="9" height="5" rx="1" fill="#27aae1"/><circle cx="8" cy="12" r="1.4" fill="#fff"/></svg>(US): 1(555)316-2947</li>
        <li><svg viewBox="0 0 16 16"><path d="M1 7 Q8 1 15 7 L13 9 L11 7.5 L11 6 Q8 5 5 6 L5 7.5 L3 9 Z" fill="#27aae1"/><rect x="3.5" y="9.5" width="9" height="5" rx="1" fill="#27aae1"/><circle cx="8" cy="12" r="1.4" fill="#fff"/></svg>(RUS): 7(955)482-3170</li>
      </ul>

      <p class="details__second-role">Real Estate Investor<br>Marrowfield, QT</p>
    </div>
  </section>
</body>
</html>
```